UI improvement for an existing app

Hi, we have a mobile preorder app that was built with standard flutter UI.

Looking at improving the whole look and feel of our app and make it look more slick and on trend. Something similar to zestcart, Platemoor or something along these lines.

Keeping in mind that we are white labeling our app so it needs to be easily redline for other clients.

For our first client I've attached their branding guideline in this project as well.

Please find all the existing screen of our app which we are looking to improve.

Main focus is to give the app a modern and fresh look while making it easy to realign. Do ensure user experience and how they navigate the app is important

Feel free to let me know if you have any questions.

Thanks
RK

Need extra days to review

• All the functionality layout on the screenshot. There's some element that we would like to incorporate such as

1. Coupon code in checkout screen
2. Allow users to edit their profile in profile page

```html
<!DOCTYPE html>
<html lang="en">
<head>
<meta charset="utf-8">
<title>Drink Detail and Preferences Screens</title>
<link href="https://fonts.googleapis.com/css2?family=Catamaran:wght@300;400;500;600;700&display=swap" rel="stylesheet">
<style>
  :root {
    --canvas: #e2e2e2;
    --overlay-grey: #a09b9e;
    --search-grey: #999497;
    --ink: #111111;
    --card: #fafafa;
    --leaf: #7db83e;
    --forest: #5b8a29;
    --forest-dark: #4e7330;
    --forest-soft: #6a9a41;
    --lime: #cbdc3b;
    --chip-grey: #b9b9b9;
    --knob-grey: #c4c4c4;
    --white: #ffffff;
    --buy-green: #8cc63f;
    --cup-icon: #9bb62e;
  }
  * { box-sizing: border-box; margin: 0; padding: 0; }
  html, body { width: 1200px; height: 1200px; overflow: hidden; }
  body {
    background: var(--canvas);
    font-family: "Catamaran", sans-serif;
    position: relative;
  }
  .screen { position: absolute; top: 84px; width: 477px; height: 1032px; overflow: hidden; }

  /* Detail screen */
  .detail { left: 84px; background: var(--overlay-grey); }
  .detail .page-title { position: absolute; left: 30px; top: 40px; font-size: 33px; font-weight: 700; color: var(--ink); }
  .search-bar {
    position: absolute; left: 13px; top: 97px; width: 449px; height: 63px;
    border-radius: 32px; background: var(--search-grey);
    display: flex; align-items: center; padding: 0 22px;
  }
  .search-bar .placeholder { margin-left: 10px; font-size: 15px; color: #777; flex: 1; }
  .product-card {
    position: absolute; left: 0; top: 218px; width: 477px; height: 814px;
    background: var(--card); border-radius: 52px 52px 0 0; text-align: center;
  }
  .product-card .name { position: absolute; left: 0; right: 0; top: 36px; font-size: 30px; font-weight: 700; color: var(--ink); line-height: 44px; }
  .product-card .tagline { position: absolute; left: 0; right: 0; top: 82px; font-size: 23.5px; font-weight: 400; color: #222; letter-spacing: 0.5px; line-height: 36px; }
  .product-photo {
    position: absolute; left: 179px; top: 151px; width: 126px; height: 289px;
    border-radius: 10px 10px 34px 34px;
    background: linear-gradient(180deg, #f6c75a 0%, #ec9d1c 55%, #d97c0c 100%);
  }
  .product-card .description {
    position: absolute; left: 0; right: 0; top: 490px;
    font-size: 16.5px; line-height: 32px; color: #222; letter-spacing: 0.6px; white-space: nowrap;
  }
  .preferences-tab {
    position: absolute; left: 0; bottom: 0; width: 477px; height: 96px;
    background: var(--leaf); border-radius: 45px 45px 0 0;
    text-align: center; color: var(--white);
  }
  .preferences-tab svg { margin-top: 10px; }
  .preferences-tab .label { font-size: 23px; font-weight: 500; margin-top: -2px; }

  /* Preferences screen */
  .prefs { left: 639px; background: var(--lime); }
  .prefs-header {
    position: absolute; left: 0; top: 0; width: 477px; height: 94px;
    background: var(--card); border-radius: 0 0 56px 56px;
  }
  .thumb { position: absolute; left: 83px; top: 17px; width: 25px; height: 56px; border-radius: 3px 3px 8px 8px;
    background: linear-gradient(180deg, #f4c252, #e08a12); }
  .prefs-header .name { position: absolute; left: 134px; top: 27px; font-size: 25px; font-weight: 700; color: var(--ink); }
  .options-panel {
    position: absolute; left: 0; top: 117px; width: 477px; height: 915px;
    background: var(--forest); border-radius: 62px 62px 0 0;
  }
  .chevron { position: absolute; left: 232px; top: 138px; }
  .question { position: absolute; left: 58px; font-size: 22.5px; font-weight: 600; color: var(--white); letter-spacing: 0.4px; line-height: 30px; white-space: nowrap; }
  .size-option {
    position: absolute; top: 271px; width: 91px; height: 90px; border-radius: 28px;
    background: var(--forest-dark); display: flex; align-items: center; justify-content: center;
  }
  .size-option.selected { background: var(--forest-soft); }
  .size-dot {
    border-radius: 50%; background: var(--knob-grey); display: flex; align-items: center; justify-content: center;
    font-weight: 700; font-size: 20px; color: var(--ink); box-shadow: 0 3px 6px rgba(0,0,0,0.25);
  }
  .size-option.selected .size-dot { background: var(--white); }
  .slider-track { position: absolute; left: 48px; top: 479px; width: 369px; height: 6px; border-radius: 3px; background: var(--white); }
  .slider-fill { position: absolute; left: 0; top: 0; width: 104px; height: 6px; border-radius: 3px; background: var(--lime); }
  .slider-knob { position: absolute; left: 143px; top: 468px; width: 28px; height: 28px; border-radius: 50%;
    background: var(--white); border: 3px solid #ddd; box-shadow: 0 2px 5px rgba(0,0,0,0.3); }
  .slider-label { position: absolute; top: 512px; font-size: 13px; font-weight: 700; color: var(--white); transform: translateX(-50%); line-height: 18px; }
  .temp-option {
    position: absolute; top: 641px; width: 80px; height: 81px; border-radius: 26px;
    background: var(--chip-grey); display: flex; align-items: center; justify-content: center;
  }
  .temp-option.selected { background: var(--white); }
  .info-pill {
    position: absolute; left: 33px; width: 419px; height: 63px; border-radius: 32px;
    background: var(--white); display: flex; align-items: center; justify-content: space-between;
    padding: 0 24px; color: var(--ink); font-weight: 700;
  }
  .quantity { top: 780px; font-size: 21px; }
  .stepper { display: flex; align-items: center; gap: 12px; font-size: 20px; }
  .total { top: 858px; font-size: 25px; }
  .total .price { font-size: 31px; }
  .action {
    position: absolute; top: 944px; height: 60px; border-radius: 30px;
    display: flex; align-items: center; justify-content: center; font-size: 20px; font-weight: 600;
  }
  .add-to-cart { left: 26px; width: 199px; border: 3px solid var(--white); color: var(--white); }
  .buy-now { left: 252px; width: 200px; background: var(--white); color: var(--buy-green); }
</style>
</head>
<body>

<section class="screen detail">
  <h1 class="page-title">Drinks</h1>
  <div class="search-bar">
    <svg width="22" height="22" viewBox="0 0 22 22"><circle cx="9" cy="9" r="7" fill="none" stroke="#6e6a6c" stroke-width="2.2"/><line x1="14" y1="14" x2="20" y2="20" stroke="#6e6a6c" stroke-width="2.4" stroke-linecap="round"/></svg>
    <span class="placeholder">Find your Drink</span>
    <svg width="26" height="20" viewBox="0 0 26 20"><g stroke="#1a1a1a" stroke-width="2.4" stroke-linecap="round"><line x1="2" y1="3" x2="24" y2="3"/><line x1="6" y1="10" x2="20" y2="10"/><line x1="10" y1="17" x2="16" y2="17"/></g></svg>
  </div>
  <article class="product-card">
    <h2 class="name">Signature Fruit Tea</h2>
    <p class="tagline">Fruity Refreshment</p>
    <div class="product-photo" role="img" aria-label="Iced orange and peach fruit tea in a tall clear cup"></div>
    <p class="description">Signature Fruit Tea is a delicious tea<br>made on the house with Orange and Peach<br>as the main ingredients. They add up to<br>give a bright orange spark to make our<br>customers yearn towards it.</p>
    <div class="preferences-tab">
      <svg width="14" height="18" viewBox="0 0 14 18"><g fill="none" stroke="#fff" stroke-width="2.2" stroke-linecap="round"><polyline points="2,8 7,3 12,8"/><polyline points="2,15 7,10 12,15"/></g></svg>
      <div class="label">Preferences</div>
    </div>
  </article>
</section>

<section class="screen prefs">
  <header class="prefs-header">
    <div class="thumb" role="img" aria-label="Fruit tea cup thumbnail"></div>
    <h2 class="name">Signature Fruit Tea</h2>
  </header>
  <div class="options-panel"></div>

  <svg class="chevron" width="14" height="18" viewBox="0 0 14 18"><g fill="none" stroke="#fff" stroke-width="2" stroke-linecap="round"><polyline points="2,8 7,3 12,8"/><polyline points="2,15 7,10 12,15"/></g></svg>

  <p class="question" style="top:221px">You want small one or a big one?</p>
  <div class="size-option" style="left:58px"><div class="size-dot" style="width:42px;height:42px">S</div></div>
  <div class="size-option selected" style="left:180px"><div class="size-dot" style="width:60px;height:60px">M</div></div>
  <div class="size-option" style="left:310px"><div class="size-dot" style="width:72px;height:72px">L</div></div>

  <p class="question" style="top:420px">More sweetness brings more whizzzz!</p>
  <div class="slider-track"><div class="slider-fill"></div></div>
  <div class="slider-knob"></div>
  <span class="slider-label" style="left:73px">100%</span>
  <span class="slider-label" style="left:157px">75%</span>
  <span class="slider-label" style="left:238px">50%</span>
  <span class="slider-label" style="left:319px">25%</span>
  <span class="slider-label" style="left:397px">0%</span>

  <p class="question" style="top:591px">Wanna chill it up?</p>
  <div class="temp-option" style="left:58px">
    <svg width="28" height="38" viewBox="0 0 28 38"><line x1="16" y1="6" x2="24" y2="2" stroke="var(--cup-icon)" stroke-width="2"/><rect x="3" y="7" width="22" height="3" fill="var(--cup-icon)"/><path d="M4 12 H24 L21 36 H7 Z" fill="var(--cup-icon)"/><rect x="8" y="16" width="5" height="5" fill="#fff"/><rect x="14" y="21" width="5" height="5" fill="#fff"/><rect x="8" y="26" width="5" height="5" fill="#fff"/></svg>
  </div>
  <div class="temp-option selected" style="left:155px">
    <svg width="28" height="38" viewBox="0 0 28 38"><line x1="16" y1="6" x2="24" y2="2" stroke="var(--lime)" stroke-width="2"/><rect x="3" y="7" width="22" height="3" fill="var(--lime)"/><path d="M4 12 H24 L21 36 H7 Z" fill="var(--lime)"/><rect x="12" y="17" width="5" height="5" fill="#fff"/><rect x="9" y="25" width="5" height="5" fill="#fff"/></svg>
  </div>
  <div class="temp-option" style="left:250px">
    <svg width="28" height="38" viewBox="0 0 28 38"><line x1="16" y1="6" x2="24" y2="2" stroke="var(--cup-icon)" stroke-width="2"/><rect x="3" y="7" width="22" height="3" fill="var(--cup-icon)"/><path d="M4 12 H24 L21 36 H7 Z" fill="var(--cup-icon)"/></svg>
  </div>
  <div class="temp-option" style="left:347px">
    <svg width="28" height="44" viewBox="0 0 28 44"><g fill="none" stroke="var(--cup-icon)" stroke-width="1.5"><path d="M10 2 q-2 2 0 4 q2 2 0 4"/><path d="M14 2 q-2 2 0 4 q2 2 0 4"/><path d="M18 2 q-2 2 0 4 q2 2 0 4"/></g><rect x="3" y="13" width="22" height="3" fill="var(--cup-icon)"/><path d="M4 18 H24 L21 42 H7 Z" fill="var(--cup-icon)"/></svg>
  </div>

  <div class="info-pill quantity">
    <span>Quantity :</span>
    <span class="stepper">
      <svg width="18" height="18" viewBox="0 0 18 18"><rect width="18" height="18" rx="2" fill="#111"/><path d="M9 4v10M4 9h10" stroke="#fff" stroke-width="2.4"/></svg>
      <span>1x</span>
      <svg width="18" height="18" viewBox="0 0 18 18"><rect width="18" height="18" rx="2" fill="#111"/><path d="M4 9h10" stroke="#fff" stroke-width="2.4"/></svg>
    </span>
  </div>
  <div class="info-pill total">
    <span>Item Total :</span>
    <span class="price">$ 1.11</span>
  </div>

  <div class="action add-to-cart">Add To Cart</div>
  <div class="action buy-now">Buy Now</div>
</section>

</body>
</html>
```